Business Card

I need a business card that really pops for a potential customer or person who refers a personal injury lead. I want to highlight our office locations, but only address that needs to be on the card is my office's main address. I want a sleek, modern and minimalist design.

```html
<!DOCTYPE html>
<html lang="en">
<head>
<meta charset="utf-8">
<title>Prairie Injury Lawyers – Business Card</title>
<link rel="stylesheet" href="https://fonts.googleapis.com/css2?family=Montserrat:wght@400;500;700&display=swap">
<style>
  :root {
    --backdrop: #2c2c2c;
    --card-white: #ffffff;
    --card-dark: #3a3a3a;
    --ink: #333333;
    --band: #3b3b3b;
    --band-text: #ffffff;
    --emboss: #2e2e2e;
  }
  * { margin: 0; padding: 0; box-sizing: border-box; }
  html, body {
    width: 1200px; height: 1059px; overflow: hidden;
    background: var(--backdrop);
    font-family: "Montserrat", sans-serif;
    color: var(--ink);
  }
  .canvas { position: relative; width: 1200px; height: 1059px; }

  .card {
    position: absolute; left: 256px; width: 688px; height: 391px;
    border-radius: 16px; overflow: hidden;
  }
  .card--front { top: 100px; background: var(--card-white); }
  .card--back  { top: 537px; background: var(--card-dark); }

  .front__tab {
    position: absolute; left: 0; top: 162px; width: 12px; height: 67px;
    background: var(--band);
  }

  /* Firm name placeholder: one colour, one weight, plain tracking */
  .firm-name {
    position: absolute; display: flex; align-items: center; gap: 10px;
    font-weight: 500; color: var(--ink); white-space: nowrap; line-height: 1;
  }
  .firm-name__mark { width: 14px; height: 14px; background: currentColor; flex: none; }
  .card--front .firm-name { left: 44px; top: 184px; font-size: 21px; }
  .card--back .firm-name {
    left: 0; right: 0; top: 174px; justify-content: center;
    font-size: 40px; color: var(--emboss); gap: 18px;
  }
  .card--back .firm-name__mark { width: 26px; height: 26px; }

  .person {
    position: absolute; left: 344px; top: 100px; height: 39px;
    border-left: 2px solid var(--ink); padding-left: 14px;
  }
  .person__name { font-weight: 700; font-size: 30px; line-height: 24px; letter-spacing: 0.02em; }
  .person__title { font-weight: 400; font-size: 16px; line-height: 16px; margin-top: 2px; letter-spacing: 0.03em; }

  .address-band {
    position: absolute; left: 344px; right: 0; top: 169px; height: 52px;
    background: var(--band); color: var(--band-text); font-style: normal;
    padding: 7px 0 0 15px; font-size: 15.5px; line-height: 20px; letter-spacing: 0.02em;
  }

  .contacts {
    position: absolute; left: 344px; top: 255px; height: 63px;
    border-left: 2px solid var(--ink); padding-left: 13px;
    list-style: none; font-size: 15.5px; letter-spacing: 0.02em;
  }
  .contacts li { display: flex; align-items: center; height: 21px; line-height: 21px; margin-bottom: 4px; }
  .contacts li:last-child { margin-bottom: 0; }
  .contacts svg { width: 13px; height: 13px; margin-right: 8px; fill: var(--ink); flex: none; }
</style>
</head>
<body>
<main class="canvas">
  <section class="card card--front" aria-label="Business card front">
    <div class="front__tab"></div>
    <p class="firm-name"><span class="firm-name__mark"></span>Prairie Injury Lawyers</p>

    <div class="person">
      <p class="person__name">DANIEL REYES</p>
      <p class="person__title">MANAGER</p>
    </div>

    <address class="address-band">
      2250 North Lake Avenue<br>
      Your Country, MN 46120
    </address>

    <ul class="contacts">
      <li>
        <svg viewBox="0 0 24 24" aria-hidden="true"><path d="M6.6 10.8a15.1 15.1 0 0 0 6.6 6.6l2.2-2.2c.3-.3.7-.4 1-.2 1.1.4 2.3.6 3.6.6.6 0 1 .4 1 1V20c0 .6-.4 1-1 1A17 17 0 0 1 3 4c0-.6.4-1 1-1h3.5c.6 0 1 .4 1 1 0 1.3.2 2.5.6 3.6.1.3 0 .7-.2 1z"/></svg>
        (312)555-0148
      </li>
      <li>
        <svg viewBox="0 0 24 24" aria-hidden="true"><path d="M2 5h20v2l-10 6L2 7z"/><path d="M2 9l10 6 10-6v10H2z"/></svg>
        info@youremail.com
      </li>
      <li>
        <svg viewBox="0 0 24 24" aria-hidden="true"><path d="M12 2a10 10 0 1 0 0 20 10 10 0 0 0 0-20zm6.9 9h-3a15 15 0 0 0-1.3-6.1A8 8 0 0 1 18.9 11zM12 4c1 1.3 1.8 3.9 1.9 7h-3.8C10.2 7.9 11 5.3 12 4zM9.4 4.9A15 15 0 0 0 8.1 11h-3a8 8 0 0 1 4.3-6.1zM5.1 13h3a15 15 0 0 0 1.3 6.1A8 8 0 0 1 5.1 13zM12 20c-1-1.3-1.8-3.9-1.9-7h3.8c-.1 3.1-.9 5.7-1.9 7zm2.6-.9a15 15 0 0 0 1.3-6.1h3a8 8 0 0 1-4.3 6.1z"/></svg>
        www.yourwebsite.com
      </li>
    </ul>
  </section>

  <section class="card card--back" aria-label="Business card back">
    <p class="firm-name"><span class="firm-name__mark"></span>Prairie Injury Lawyers</p>
  </section>
</main>
</body>
</html>
```